ALL TEXT Social Media Graphics

We are looking for a series of social media graphics for Instagram (new size: 4:5 (1080 x 1350 pixels) ratio that are ALL TEXT. We want the following quotes below on each graphic; one quote per graphic. AND, In very small letters at the bottom of each graphic, add @PaulaWrenLive
The look and feel of these graphics should be complimentary to the color palette attached below; but keep them simple. But the design is up to you; at the end of this document, I provided various samples of all text graphics that I like as examples.
The Quotes are in the attached WORD document
women trying to lose weight

```html
<!DOCTYPE html>
<html lang="en">
<head>
<meta charset="utf-8">
<title>Glow Up Sunshine Reset – Social Graphics</title>
<link rel="stylesheet" href="https://fonts.googleapis.com/css2?family=Oswald:wght@500;600;700&family=Poppins:wght@400;500;600;700&display=swap">
<style>
  :root {
    --berry: #ad1457;
    --deep: #b0135a;
    --pink: #ec5a8f;
    --soft-pink: #f7a6c3;
    --ink: #161616;
  }
  * { margin: 0; padding: 0; box-sizing: border-box; }
  html, body { width: 1200px; height: 3589px; overflow: hidden; }
  body {
    position: relative;
    background: var(--berry);
    font-family: "Poppins", sans-serif;
    color: var(--ink);
  }
  .card {
    position: absolute;
    width: 498px;
    height: 622px;
    background: radial-gradient(ellipse at 30% 20%, #f8f8f8 0%, #efefef 55%, #f5f5f5 100%);
  }
  .card::after {
    content: "";
    position: absolute;
    left: 10%; right: 10%; bottom: -18px;
    height: 16px;
    border-radius: 50%;
    background: radial-gradient(ellipse at center, rgba(40,0,15,.55) 0%, rgba(40,0,15,0) 70%);
  }
  .col-l { left: 78px; } .col-r { left: 624px; }
  .row-1 { top: 72px; } .row-2 { top: 771px; } .row-3 { top: 1468px; } .row-4 { top: 2167px; } .row-5 { top: 2866px; }
  .content { position: absolute; left: 32px; right: 20px; }
  .handle { position: absolute; left: 34px; top: 562px; font-size: 14px; font-weight: 600; }
  p { line-height: 1.18; }
  .cond { font-family: "Oswald", sans-serif; font-weight: 700; line-height: 1.08; letter-spacing: .2px; }
  .pink { color: var(--pink); } .deep { color: var(--deep); }
  .rule { display: block; height: 4px; margin-top: 6px; }
  .pink-bg { background: var(--pink); } .deep-bg { background: var(--deep); } .ink-bg { background: var(--ink); }
  .block { display: inline-block; padding: 0 6px 0 2px; color: #fff; }
  .w5 { font-weight: 500; } .w6 { font-weight: 600; } .w7 { font-weight: 700; }
</style>
</head>
<body>

<section class="card col-l row-1">
  <div class="content" style="top:160px">
    <p class="w5" style="font-size:17px">YOU CAN ABSOLUTELY BE DOWN</p>
    <p class="w6 pink" style="font-size:43px;line-height:1">20–30 POUNDS</p>
    <p class="w6 deep" style="font-size:24px;line-height:1.05">BY END OF SUMMER.</p>
    <span class="rule pink-bg" style="width:182px"></span>
    <p class="w5" style="font-size:22px;margin-top:30px">All It Takes Is The Right Plan<br>And You’ve Found It.</p>
    <p class="cond" style="font-size:31px;margin-top:26px;font-weight:500">Comment <span class="pink">“Glow Up”</span> For The<br>Glow Up Sunshine Reset!</p>
  </div>
  <p class="handle">@PaulaWrenLive</p>
</section>

<section class="card col-r row-1">
  <div class="content" style="top:138px">
    <p class="w5" style="font-size:17px">YOU DON’T NEED ANOTHER DIET</p>
    <p class="w7 pink" style="font-size:36px;line-height:1">YOU NEED A SYSTEM</p>
    <p class="w7" style="font-size:32px;line-height:1"><span class="block pink-bg">THAT WORKS.</span></p>
    <p class="w5" style="font-size:20px;margin-top:26px">Drop 30 Pounds with the</p>
    <p class="cond deep" style="font-size:39px">GLOW UP SUNSHINE<br>RESET.</p>
    <span class="rule pink-bg" style="width:184px"></span>
    <p class="w5" style="font-size:20px;margin-top:28px">Comment “Summer” To</p>
    <p class="cond pink" style="font-size:46px">START NOW.</p>
  </div>
  <p class="handle">@PaulaWrenLive</p>
</section>

<section class="card col-l row-2">
  <div class="content" style="top:126px">
    <p class="w5 pink" style="font-size:30px;line-height:1.05">This Summer Ain’t Over</p>
    <p class="w5" style="font-size:18px">and neither are your body goals.</p>
    <p class="w5" style="font-size:20px;margin-top:30px">Drop 30 Pounds with the</p>
    <p class="cond pink" style="font-size:39px">GLOW UP SUNSHINE<br>RESET.</p>
    <span class="rule pink-bg" style="width:184px"></span>
    <p class="cond" style="font-size:33px;margin-top:32px">COMMENT</p>
    <p class="cond deep" style="font-size:46px;line-height:1">“GLOW UP”</p>
    <p class="cond" style="font-size:28px">TO GET THE PLAN</p>
  </div>
  <p class="handle">@PaulaWrenLive</p>
</section>

<section class="card col-r row-2">
  <div class="content" style="top:128px">
    <p class="w6 deep" style="font-size:28px">If Your Goal is a Tiny Waist,<br>Flat Belly</p>
    <p class="w7 deep" style="font-size:28px;margin-top:8px">and 30 Pounds</p>
    <p class="w5" style="font-size:28px">Down—this is the Plan.</p>
    <p class="w5" style="font-size:28px;margin-top:56px">COMMENT <span class="pink">“SUMMER”</span></p>
    <p class="w5" style="font-size:21px">To Join The Glow Up</p>
    <p class="cond pink" style="font-size:46px">SUNSHINE RESET!</p>
    <span class="rule pink-bg" style="width:288px"></span>
  </div>
  <p class="handle">@PaulaWrenLive</p>
</section>

<section class="card col-l row-3">
  <div class="content" style="top:132px;left:42px">
    <p class="w5" style="font-size:30px">There’s still time to drop the<br>30 pounds and slay<br>this summer.</p>
    <span class="rule ink-bg" style="width:198px;margin-top:2px"></span>
    <p class="w6 pink" style="font-size:45px;margin-top:36px;line-height:1.05">The Glow Up</p>
    <p class="w5" style="font-size:24px">Sunshine Reset has the<br>blueprint.</p>
    <p class="w5" style="font-size:28px;margin-top:36px">Comment <span class="pink w6">“Glow Up”!</span></p>
  </div>
  <p class="handle" style="left:42px">@PaulaWrenLive</p>
</section>

<section class="card col-r row-3">
  <div class="content" style="top:102px">
    <p class="w5" style="font-size:26px">Snatched waist,<br>flat tummy</p>
    <p class="cond deep" style="font-size:60px;margin-top:8px;line-height:1.02">30 POUNDS</p>
    <p class="cond pink" style="font-size:60px;line-height:1.02">LIGHTER</p>
    <span class="rule pink-bg" style="width:172px"></span>
    <p class="w5" style="font-size:26px;margin-top:20px">that’s what the Glow Up<br><span class="deep">Sunshine Reset</span><br>Challenge Delivers.</p>
    <p class="w5" style="font-size:26px;margin-top:28px">Comment <span class="deep w6">“Glow Up”</span><br>To Get the Plan</p>
  </div>
  <p class="handle">@PaulaWrenLive</p>
</section>

<section class="card col-l row-4">
  <div class="content" style="top:98px;left:38px">
    <p class="w6 deep" style="font-size:26px;line-height:1.15">Nothing Feels Better Than</p>
    <p class="w5" style="font-size:26px;line-height:1.15">Seeing that Scale Drop</p>
    <p class="w5" style="font-size:20px">week after week.</p>
    <p class="w5" style="font-size:20px;margin-top:28px">LET’S LOSE UP TO</p>
    <p class="cond deep" style="font-size:66px;line-height:1">30 POUNDS</p>
    <p class="cond" style="font-size:35px;line-height:1.05"><span class="block deep-bg" style="color:var(--soft-pink)">THIS SUMMER-TOGETHER.</span></p>
    <p class="w5" style="font-size:27px;margin-top:64px">Comment <span class="pink">“Summer”</span><br>To Join the Glow Up Sunshine<br>Reset!</p>
  </div>
  <p class="handle" style="left:38px">@PaulaWrenLive</p>
</section>

<section class="card col-r row-4">
  <div class="content" style="top:146px">
    <p class="cond deep" style="font-size:64px;line-height:1">Sis,</p>
    <p class="w5" style="font-size:21px;margin-top:4px">we’re dropping belly flat and</p>
    <p class="w6 pink" style="font-size:27px">Saying Goodbye to</p>
    <p class="w6 deep" style="font-size:23px">Stubborn Pounds.</p>
    <span class="rule deep-bg" style="width:172px"></span>
    <p class="w6 deep" style="font-size:29px;margin-top:56px">Join the Glow Up</p>
    <p class="w5" style="font-size:28px">Sunshine Reset</p>
    <p class="w5" style="font-size:21px">Comment “Summer”!</p>
  </div>
  <p class="handle">@PaulaWrenLive</p>
</section>

<section class="card col-l row-5">
  <div class="content" style="top:142px">
    <p class="w5" style="font-size:21px">Don’t wait ’til</p>
    <p class="w6 pink" style="font-size:35px;line-height:1">Next Summer</p>
    <p class="w5" style="font-size:25px">To Get Right.</p>
    <p class="cond" style="font-size:40px;margin-top:12px">THE TIME IS NOW.</p>
    <p class="cond deep" style="font-size:55px;line-height:1">DROP 30 POUNDS</p>
    <p class="w5" style="font-size:19px;margin-top:4px">with the <span class="pink w6">Glow Up Sunshine Reset.</span></p>
    <span class="rule deep-bg" style="width:352px"></span>
    <p class="w5" style="font-size:22px;margin-top:46px">Comment “Summer”!</p>
  </div>
  <p class="handle">@PaulaWrenLive</p>
</section>

<section class="card col-r row-5">
  <div class="content" style="top:146px;left:40px">
    <p class="w5" style="font-size:21px">You’ve got 8 weeks and the</p>
    <p class="cond deep" style="font-size:43px;line-height:1.05">PERFECT PLAN TO</p>
    <p class="w6" style="font-size:27px">Drop 30 Pounds.</p>
    <p class="cond pink" style="font-size:46px;margin-top:32px;line-height:1.05">LET’S GET SNATCHED</p>
    <p class="w5" style="font-size:22px">this Summer with the Glow Up</p>
    <p class="cond deep" style="font-size:36px">SUNSHINE RESET</p>
    <span class="rule deep-bg" style="width:162px"></span>
    <p class="w5" style="font-size:23px;margin-top:42px">Comment “Summer”!</p>
  </div>
  <p class="handle" style="left:40px">@PaulaWrenLive</p>
</section>

</body>
</html>
```